Dune Business Card Design Project

We have an existing business card. We are looking to creat a new card for the store. I have attached a my own business so you have a refference of what the current card looks like.

Phone: 1300 574 213
email: merrow@dunepanes.com.au
website: www.dunepanes.com.au
Address: (Inside Merrow Rug Hall) 418 Tolvey Rd, Pelbrook VIC 3158
Updates

This is a new business card for our store.

Industry/Entity Type

Business

Requirements
Must have
• Must look similar to the existing card

```html
<!DOCTYPE html>
<html lang="en">
<head>
<meta charset="utf-8">
<title>Dune Business Card</title>
<link href="https://fonts.googleapis.com/css2?family=Open+Sans:wght@400;600&display=swap" rel="stylesheet">
<style>
  :root {
    --paper: #ffffff;
    --ink: #231f20;
    --text: #3a3a3a;
    --green: #0a9f4a;
    --band-dark: #1bb26b;
    --band-light: #b8d65f;
    --shadow: rgba(0,0,0,0.55);
  }
  html, body {
    margin: 0;
    padding: 0;
    width: 1200px;
    height: 1000px;
    overflow: hidden;
    background: var(--paper);
    font-family: "Open Sans", Arial, sans-serif;
  }
  .canvas { position: relative; width: 1200px; height: 1000px; }
  .card {
    position: absolute;
    left: 277px;
    width: 645px;
    height: 350px;
    background: var(--paper);
    box-shadow: 6px 6px 6px var(--shadow), 0 0 2px rgba(0,0,0,0.08);
    overflow: hidden;
  }
  .card--front { top: 115px; }
  .card--back { top: 533px; }
  .corner-graphic {
    position: absolute;
    width: 215px;
    height: 85px;
    background: linear-gradient(90deg, var(--band-dark) 0%, var(--band-light) 50%, var(--band-dark) 100%);
  }
  .corner-graphic--top-left { left: 0; top: 0; }
  .corner-graphic--bottom-right { right: 0; bottom: 0; }
  .brand-name {
    position: absolute;
    margin: 0;
    color: var(--ink);
    font-weight: 400;
    line-height: 1;
  }
  .card--front .brand-name {
    left: 0; right: 0; top: 146px;
    text-align: center;
    font-size: 46px;
  }
  .front-web {
    position: absolute;
    left: 0; right: 0; top: 227px;
    text-align: center;
    font-size: 9px;
    font-weight: 600;
    letter-spacing: 3.2px;
    color: var(--ink);
  }
  .person { position: absolute; left: 47px; top: 33px; }
  .person__name, .person__role {
    margin: 0;
    font-size: 18px;
    line-height: 23px;
    font-weight: 400;
  }
  .person__name { color: var(--text); }
  .person__role { color: var(--green); }
  .phone {
    position: absolute;
    right: 44px;
    top: 33px;
    font-size: 14px;
    color: var(--text);
  }
  .phone .label { font-weight: 600; }
  .label { color: var(--green); }
  .card--back .brand-name {
    right: 67px; top: 170px;
    font-size: 62px;
  }
  .contact {
    position: absolute;
    left: 47px;
    top: 226px;
    font-size: 9.5px;
    letter-spacing: 0.9px;
    color: var(--text);
    font-weight: 400;
  }
  .contact p { margin: 0; line-height: 19px; }
  .contact .label { font-weight: 600; }
  .contact .tight { line-height: 16px; }
</style>
</head>
<body>
<div class="canvas">

  <section class="card card--front">
    <div class="corner-graphic corner-graphic--top-left" role="img" aria-label="Green diagonal stripe graphic"></div>
    <h1 class="brand-name">Dune</h1>
    <div class="front-web">www.dunepanes.com.au</div>
    <div class="corner-graphic corner-graphic--bottom-right" role="img" aria-label="Green diagonal stripe graphic"></div>
  </section>

  <section class="card card--back">
    <div class="person">
      <p class="person__name">Aaron Welby</p>
      <p class="person__role">Director</p>
    </div>
    <div class="phone"><span class="label">Phone:</span> 1300 574 213</div>
    <h2 class="brand-name">Dune</h2>
    <div class="contact">
      <p class="label">Address:</p>
      <p>(Inside Merrow Rug Hall)</p>
      <p>418 Tolvey Rd,</p>
      <p>Pelbrook VIC 3158</p>
      <p class="tight"><span class="label">email:</span> merrow@dunepanes.com.au</p>
      <p class="tight"><span class="label">website:</span> www.dunepanes.com.au</p>
    </div>
    <div class="corner-graphic corner-graphic--bottom-right" role="img" aria-label="Green diagonal stripe graphic"></div>
  </section>

</div>
</body>
</html>
```